Fahnendesign für netzkastenverleih.de
Zielgruppe
netzkastenverleih.de vermietet Baustromverteiler an Bauunternehmen und private Bauherren.
Wir liefern die Verteiler, stellen sie auf und führen Terminabsprachen mit den örtlichen Energieversorgern.
Aufgabenstellung
-Nach Druckvorgabe Druckfalke ( Befestigung links)
-Logo soll groß zu sehen sein
Die Fahne kann schlicht gehalten werden. Gerne aber auch eigene Ideen mit einbringen.
- Unternehmensschrift: Titel Fira Sans , Schrift : Montserrat

```html
<!DOCTYPE html>
<html lang="de">
<head>
<meta charset="utf-8">
<title>Fahne netzkastenverleih.de</title>
<link rel="stylesheet" href="https://fonts.googleapis.com/css2?family=Fira+Sans:wght@500&family=Montserrat:wght@400&display=swap">
<style>
  :root {
    --brand-blue: #11518c;
    --brand-orange: #f29a10;
    --paper: #ffffff;
    --stage: #ffffff;
  }
  html, body {
    margin: 0;
    padding: 0;
    width: 1081px;
    height: 1200px;
    overflow: hidden;
    background: var(--stage);
  }
  .flag {
    position: absolute;
    left: 348px;
    top: 107px;
    width: 382px;
    height: 1017px;
    background: var(--paper);
    box-shadow: 0 0 14px rgba(0,0,0,0.06);
    overflow: hidden;
  }
  .flag-backdrop {
    position: absolute;
    inset: 0;
  }
  .brand {
    position: absolute;
    left: 0;
    top: 0;
    width: 100%;
    text-align: center;
  }
  .brand-mark {
    position: absolute;
    left: 131px;
    top: 92px;
    width: 120px;
    height: 120px;
    background: var(--brand-orange);
  }
  .brand-name {
    position: absolute;
    left: 0;
    top: 298px;
    width: 100%;
    margin: 0;
    font-family: "Fira Sans", sans-serif;
    font-weight: 500;
    font-size: 28px;
    letter-spacing: 0.2px;
    color: var(--brand-blue);
  }
  .contact-list {
    position: absolute;
    left: 0;
    top: 0;
    margin: 0;
    padding: 0;
    list-style: none;
  }
  .contact-item {
    position: absolute;
    left: 0;
    width: 382px;
    height: 36px;
  }
  .contact-icon {
    position: absolute;
    left: 24px;
    top: 1px;
    width: 34px;
    height: 34px;
  }
  .contact-text {
    position: absolute;
    left: 104px;
    top: 6px;
    font-family: "Montserrat", sans-serif;
    font-weight: 400;
    font-size: 19.5px;
    color: var(--paper);
    white-space: nowrap;
  }
  .contact-web { top: 663px; }
  .contact-photo { top: 734px; }
  .contact-social { top: 806px; }
</style>
</head>
<body>
  <main class="flag">
    <svg class="flag-backdrop" width="382" height="1017" viewBox="0 0 382 1017" aria-hidden="true">
      <polygon points="80,482 382,407 382,1017 82,1017" fill="var(--brand-blue)"/>
      <polygon points="0,500 80,482 82,1017 0,1017" fill="var(--brand-orange)"/>
    </svg>

    <header class="brand">
      <div class="brand-mark" aria-hidden="true"></div>
      <h1 class="brand-name">netzkastenverleih.de</h1>
    </header>

    <ul class="contact-list">
      <li class="contact-item contact-web">
        <svg class="contact-icon" viewBox="0 0 34 34" aria-hidden="true">
          <circle cx="17" cy="17" r="14.5" fill="none" stroke="#fff" stroke-width="3"/>
          <ellipse cx="17" cy="17" rx="6" ry="14.5" fill="none" stroke="#fff" stroke-width="3"/>
          <line x1="3" y1="17" x2="31" y2="17" stroke="#fff" stroke-width="3"/>
        </svg>
        <span class="contact-text">www.netzkastenverleih.de</span>
      </li>
      <li class="contact-item contact-photo">
        <svg class="contact-icon" viewBox="0 0 34 34" aria-hidden="true">
          <circle cx="17" cy="17" r="15" fill="#fff"/>
        </svg>
        <span class="contact-text">netzkastenverleih.de</span>
      </li>
      <li class="contact-item contact-social">
        <svg class="contact-icon" viewBox="0 0 34 34" aria-hidden="true">
          <circle cx="17" cy="17" r="17" fill="#fff"/>
        </svg>
        <span class="contact-text">@netzkastenverleih.de</span>
      </li>
    </ul>
  </main>
</body>
</html>
```